依頼詳細
既存サイトのデザインが古くなったため、リニューアルを行います。
ワイヤーフレーム有。
参考サイト有。
https://www.morisuzu-web.jp/
今風でシンプルなデザインをお願いいたします。
メインカラーは緑で、現在のロゴをお渡ししますので、トレースしSVGで作ってください。
サイトURL
ページ数
1ページ
希望イメージ
シンプル 複雑
単色 カラフル
暗い 明るい
日常 高級
遊び心 厳粛
未来的 伝統的
女性的 男性的
希望する色
緑系
納品ファイル
• イラストレーター形式 (.ai)
補足説明
TOPページ(PC版とスマホ版)のみご提案ください。
採用した場合は、アーカイブと詳細ページ(スタイルガイド)のデザインもお願いいたします。
ワイヤーフレームではなく、サイトマップ有です。
締め切りを10日後に変更しました。
URLの記載があるのは、参考サイトです。
会社名はダミー(株式会社ダミーリサイクル)とし、
添付のサイトマップに合わせて作っていただけると幸いです。
記載内容がややこしくて申し訳ございません。
その他文言等もダミーで結構です。
よろしくお願いいたします。
■ 選んだ理由

シンプルかつ、今風なレイアウトで好感が持てました。

■ 提案者全員のお礼・コメント

修正依頼にも迅速に対応いただき、ありがとうございました。
またご提案よろしくお願いいたします。

```html
<!DOCTYPE html>
<html lang="ja">
<head>
<meta charset="UTF-8">
<title>株式会社ダミーリサイクル</title>
<link href="https://fonts.googleapis.com/css2?family=Noto+Sans+JP:wght@400;500;700;900&family=Montserrat:wght@500;600;700&display=swap" rel="stylesheet">
<style>
:root{
  --green:#4caf3a;
  --green-dark:#3a8f2c;
  --ink:#333333;
  --dark:#454545;
  --darker:#3a3a3a;
  --light:#f3f3f3;
  --white:#ffffff;
  --muted:#888888;
}
*{margin:0;padding:0;box-sizing:border-box}
html,body{width:1200px;height:4352px;overflow:hidden}
body{font-family:"Noto Sans JP",sans-serif;color:var(--ink);background:var(--white);position:relative}
.en{font-family:"Montserrat",sans-serif}
.abs{position:absolute}

/* header */
.site-header{position:absolute;top:0;left:0;width:1200px;height:88px;background:var(--white)}
.brand{position:absolute;left:20px;top:10px;display:flex;align-items:center;gap:10px;font-weight:700;font-size:22px;color:var(--ink)}
.brand-dot{width:28px;height:28px;border-radius:50%;background:var(--green)}
.header-info{position:absolute;left:230px;top:10px;font-size:10px;line-height:15px;color:var(--muted)}
.header-tel{position:absolute;left:650px;top:10px;display:flex;align-items:center;gap:8px;font-size:11px;color:var(--ink);white-space:nowrap}
.header-tel strong{font-family:"Montserrat",sans-serif;font-size:24px;color:var(--green);font-weight:700}
.header-contact{position:absolute;right:0;top:0;width:178px;height:46px;background:var(--green);color:var(--white);font-size:14px;font-weight:700;display:flex;align-items:center;justify-content:center;gap:8px}
.global-nav{position:absolute;left:0;top:48px;width:1200px;height:40px;display:flex;border-top:1px solid #e4e4e4}
.global-nav a{flex:1;display:flex;align-items:center;justify-content:center;font-size:13px;color:var(--ink);text-decoration:none;border-right:1px solid #e4e4e4}
.global-nav a.nav-recruit{background:var(--green);color:var(--white);border-right:0}

/* hero */
.hero{position:absolute;top:88px;left:0;width:1200px;height:572px;background:linear-gradient(135deg,#2b2620 0%,#5a4a3a 45%,#7a6550 60%,#2a231d 100%)}
.hero-copy{position:absolute;left:140px;top:48px;color:var(--white)}
.hero-copy h1{font-size:38px;font-weight:900;line-height:56px;letter-spacing:1px}
.hero-copy .hero-en{font-family:"Montserrat",sans-serif;font-size:11px;line-height:17px;margin-top:18px;opacity:.9}
.hero-copy .hero-sub{font-size:12px;line-height:20px;margin-top:18px}

/* section headings */
.sec-label{font-size:11px;color:var(--green);font-weight:500}
.sec-title{font-family:"Montserrat",sans-serif;font-weight:700;font-size:38px;line-height:46px}
.btn{display:flex;align-items:center;justify-content:center;background:var(--green);color:var(--white);border-radius:20px;font-size:12px;font-family:"Montserrat",sans-serif;font-weight:600}

/* news */
.news{position:absolute;top:660px;left:0;width:1200px;height:640px;background:var(--light)}
.news-list{position:absolute;left:140px;top:142px;width:915px;list-style:none}
.news-item{height:62px;background:var(--white);margin-bottom:14px;display:flex;align-items:center;padding-left:44px;font-size:13px;box-shadow:0 1px 3px rgba(0,0,0,.06)}
.news-item svg{margin-right:18px}
.news-item time{font-family:"Montserrat",sans-serif;color:var(--green);width:140px;font-size:11px}

/* business */
.business{position:absolute;top:1300px;left:0;width:1200px;height:420px;background:var(--dark);color:var(--white)}
.business-card{position:absolute;top:168px;width:344px;height:164px;display:flex;flex-direction:column;align-items:center;justify-content:center}
.business-card h3{font-size:26px;font-weight:900;color:var(--white);text-shadow:0 0 6px rgba(0,0,0,.4)}
.business-card span{font-family:"Montserrat",sans-serif;font-size:11px;color:#cfe9c7;margin-top:4px}

/* company / environment */
.panel{position:absolute;background:var(--dark);color:var(--white)}
.panel p{font-size:13px;line-height:26px}
.photo{position:absolute}
.company-text{position:absolute;left:140px;top:50px;width:260px;z-index:2}
</style>
</head>
<body>

<header class="site-header">
  <div class="brand"><span class="brand-dot"></span>ダミーリサイクル</div>
  <div class="header-info">産業廃棄物中間処理・収集運搬<br>一般廃棄物収集運搬・リサイクル事業</div>
  <div class="header-tel">お電話のお問い合わせ
    <svg width="18" height="18" viewBox="0 0 24 24"><path fill="#4caf3a" d="M6.6 10.8c1.4 2.8 3.8 5.1 6.6 6.6l2.2-2.2c.3-.3.7-.4 1-.2 1.1.4 2.3.6 3.6.6.6 0 1 .4 1 1V20c0 .6-.4 1-1 1C10.6 21 3 13.4 3 4c0-.6.4-1 1-1h3.5c.6 0 1 .4 1 1 0 1.3.2 2.5.6 3.6.1.3 0 .7-.2 1z"/></svg>
    <strong>0000-000-000</strong></div>
  <div class="header-contact">
    <svg width="16" height="12" viewBox="0 0 16 12"><rect x="0.5" y="0.5" width="15" height="11" fill="none" stroke="#fff"/><path d="M1 1l7 6 7-6" fill="none" stroke="#fff"/></svg>お問い合わせ</div>
  <nav class="global-nav">
    <a href="#">会社情報</a><a href="#">事業案内</a><a href="#">新品事業</a><a href="#">リサイクル</a><a href="#">環境活動の取り組み</a><a href="#" class="nav-recruit">採用情報</a>
  </nav>
</header>

<section class="hero" role="img" aria-label="両手ですくい上げた土の写真">
  <div class="hero-copy">
    <h1>高い産業廃棄物中間処理技術<br>環境に配慮した再資源化</h1>
    <p class="hero-en">Advanced industrial waste intermediate treatment technology<br>Environmentally friendly recycling</p>
    <p class="hero-sub">地域と連携した資源循環<br>未来へつなぐ持続可能な社会へ</p>
  </div>
</section>

<section class="news">
  <div class="abs" style="left:140px;top:74px"><p class="sec-label">最新情報</p><h2 class="sec-title" style="color:var(--green)">News</h2></div>
  <ul class="news-list">
    <li class="news-item"><svg width="8" height="10"><path d="M1 1l5 4-5 4" fill="none" stroke="#4caf3a" stroke-width="1.5"/></svg><time>2024.00.00</time>ホームページをリニューアルしました</li>
    <li class="news-item"><svg width="8" height="10"><path d="M1 1l5 4-5 4" fill="none" stroke="#4caf3a" stroke-width="1.5"/></svg><time>2024.00.00</time>ホームページをリニューアルしました</li>
    <li class="news-item"><svg width="8" height="10"><path d="M1 1l5 4-5 4" fill="none" stroke="#4caf3a" stroke-width="1.5"/></svg><time>2024.00.00</time>ホームページをリニューアルしました</li>
    <li class="news-item"><svg width="8" height="10"><path d="M1 1l5 4-5 4" fill="none" stroke="#4caf3a" stroke-width="1.5"/></svg><time>2024.00.00</time>ホームページをリニューアルしました</li>
    <li class="news-item"><svg width="8" height="10"><path d="M1 1l5 4-5 4" fill="none" stroke="#4caf3a" stroke-width="1.5"/></svg><time>2024.00.00</time>ホームページをリニューアルしました</li>
  </ul>
  <div class="btn abs" style="left:888px;top:540px;width:167px;height:22px;font-size:10px">View All</div>
</section>

<section class="business">
  <div class="abs" style="left:0;top:72px;width:1200px;text-align:center"><p class="sec-label" style="color:#cfcfcf">事業案内</p><h2 class="sec-title">Business</h2></div>
  <div class="business-card" role="img" aria-label="森の木々の写真" style="left:72px;background:linear-gradient(160deg,#5f7a55,#2f4a32)"><h3>環境事業</h3><span>Environment</span></div>
  <div class="business-card" role="img" aria-label="山並みと空の風景写真" style="left:428px;background:linear-gradient(180deg,#8fb3d4,#5a7a8c 60%,#3d5a48)"><h3>運搬事業</h3><span>Transportation</span></div>
  <div class="business-card" role="img" aria-label="街並みと建物の写真" style="left:784px;background:linear-gradient(160deg,#b8a89a,#6e6158)"><h3>建築事業</h3><span>Architecture</span></div>
</section>

<section class="company">
  <div class="panel" style="left:0;top:1760px;width:640px;height:640px">
    <div class="company-text">
      <p class="sec-label">会社情報</p>
      <h2 class="sec-title">Company</h2>
      <p style="margin-top:22px">ダミー社は、昭和の創業以来地域に根ざした廃棄物処理業として、産業廃棄物の中間処理と再資源化に取り組んでまいりました。お客様の信頼にお応えし、これからも環境と調和した事業を推進してまいります。</p>
      <div class="btn" style="margin-top:30px;width:96px;height:20px;font-size:10px">More</div>
    </div>
  </div>
  <div class="photo" role="img" aria-label="霧のかかった森と岩の写真" style="left:432px;top:1828px;width:640px;height:520px;background:linear-gradient(180deg,#2f4a2f,#4e6a46 50%,#7d8a78 75%,#3a4636)"></div>
</section>

<section class="environment">
  <div class="panel" style="left:558px;top:2480px;width:642px;height:480px">
    <div class="abs" style="left:242px;top:66px;width:300px">
      <p class="sec-label">環境活動</p>
      <h2 class="sec-title">Environment</h2>
      <p style="margin-top:22px">ダミー社は、持続可能な社会の実現に向けてさまざまな活動を行っています。廃棄物の再資源化やエネルギーの効率的な利用、地域清掃活動などを通じて、地球環境の保全と次世代への豊かな自然の継承に貢献してまいります。</p>
      <div class="btn" style="margin-top:30px;width:164px;height:22px;font-size:10px">More</div>
    </div>
  </div>
  <div class="photo" role="img" aria-label="土と若葉を両手で包む写真" style="left:88px;top:2428px;width:640px;height:404px;background:linear-gradient(160deg,#e8eee2,#c7d8b8 45%,#8a6e52 75%,#d6e0cc)"></div>
</section>

<section class="recruit">
  <div class="abs" style="left:0;top:2956px;width:1200px;text-align:center">
    <p class="sec-label">採用情報</p>
    <h2 class="sec-title">Recruit</h2>
    <p style="font-size:12px;margin-top:18px">「働く喜び」を共に分かち合い、成長できる職場です。新しい仲間との出会いをお待ちしています。</p>
  </div>
  <div class="photo" role="img" aria-label="社員たちの集合写真と募集メッセージ" style="left:240px;top:3088px;width:720px;height:412px;background:linear-gradient(180deg,#c9d3d8,#8e9aa2)">
    <div class="abs" style="left:210px;top:150px;width:300px;text-align:center;font-size:36px;font-weight:900;color:var(--ink);line-height:52px;background:rgba(255,255,255,.75)">一緒に環境作りを<br>目指しています</div>
  </div>
</section>

<section class="links" style="position:absolute;top:3520px;left:0;width:1200px;height:440px;background:var(--light)">
  <div class="btn abs" style="left:160px;top:92px;width:420px;height:60px;border-radius:0;font-family:'Noto Sans JP',sans-serif;font-size:13px">会社情報</div>
  <div class="btn abs" style="left:620px;top:92px;width:432px;height:60px;border-radius:0;font-family:'Noto Sans JP',sans-serif;font-size:13px">事業案内</div>
  <div class="btn abs" style="left:160px;top:180px;width:420px;height:60px;border-radius:0;font-family:'Noto Sans JP',sans-serif;font-size:13px">新品事業</div>
  <div class="btn abs" style="left:620px;top:180px;width:432px;height:60px;border-radius:0;font-family:'Noto Sans JP',sans-serif;font-size:13px">リサイクル</div>
  <div class="abs" style="left:0;top:270px;width:1200px;text-align:center">
    <p style="font-size:11px">お問い合わせ</p>
    <p class="en" style="font-size:38px;font-weight:700;line-height:50px">0000-000-000</p>
    <p style="font-size:10px;color:var(--muted)">受付時間 8:30〜17:00（土日祝を除く）</p>
  </div>
  <div class="abs" style="left:420px;top:368px;width:368px;height:52px;border-radius:26px;background:var(--darker);color:var(--white);font-size:14px;display:flex;align-items:center;justify-content:center;gap:10px">
    <svg width="16" height="12" viewBox="0 0 16 12"><rect x="0.5" y="0.5" width="15" height="11" fill="none" stroke="#fff"/><path d="M1 1l7 6 7-6" fill="none" stroke="#fff"/></svg>Webからのお問い合わせ</div>
</section>

<footer style="position:absolute;top:3960px;left:0;width:1200px;height:392px;background:var(--dark);color:#e6e6e6;font-size:11px">
  <p class="abs" style="left:140px;top:60px">TOP</p>
  <ul class="abs" style="left:272px;top:60px;list-style:none;line-height:28px"><li>会社情報</li><li>代表挨拶</li><li>沿革</li><li>組織図</li><li>拠点情報</li><li>許可証一覧</li><li>アクセス</li><li>お知らせ</li></ul>
  <ul class="abs" style="left:472px;top:60px;list-style:none;line-height:28px"><li>事業案内</li><li>環境事業</li><li>運搬事業</li><li>建築事業</li><li>処理フロー</li></ul>
  <ul class="abs" style="left:680px;top:60px;list-style:none;line-height:28px"><li>新品事業</li><li>商品案内</li><li>導入事例</li></ul>
  <ul class="abs" style="left:880px;top:60px;list-style:none;line-height:28px"><li>リサイクル</li><li>リサイクル品</li><li>取組紹介</li></ul>
  <ul class="abs" style="left:1020px;top:60px;list-style:none;line-height:28px"><li>採用情報</li><li>環境活動の取り組み</li><li>お問い合わせ</li><li>サイトマップ</li><li>プライバシーポリシー</li></ul>
  <p class="abs" style="left:0;top:368px;width:1200px;text-align:center;font-size:9px;color:#bdbdbd">© DUMMY RECYCLE Co., Ltd.</p>
</footer>

</body>
</html>
```